Webdesign for Property Renting Business

We need a professional and slim design for a hight quality property renting website which is not overcrowded with too much information and has a clear and easily structure to read. The visitor should get an instant impression what he can do at a glance.

The goal of this contest is to get a design for building a prototype of the website and to attract our client and owner of the site by a good looking prototype and not just a wireframe. Therefore we don't need an HTML-coded design at this early project-stage. We only expect getting a simple bitmap or vector-graphic design.

Actually we don't have a logo. Use a placeholder or feel free to design a simple one by yourself.

Last but not least if you have a good idea just include it in to your design.

Our goal is to get a design for building a prototype of the website and to attract our client by a good looking prototype and not just a wireframe.

Target Market(s)

People who want to spend money to rent a good quality property. Not only the riches. These could be business people and also demanding families as well.

Industry/Entity Type

Building

Colors
85cae6

Requirements
Must have
• We need two sites, a start site and a property-details site. Each site has to include the following points:

1.) start site
- search mask (location, date to choose, quanity of guests)
- show some properties (highlights, special offers etc.)
- show login/register link

2.) property site
- Location in Vorlen Map
- Photos, Description, Amenities, Calendar (available,not available), Contact, Reviews

These are some sites which I like from a design prospective
- http://www.stayquelo.com
- http://www.lodvanta.com/
- http://www.dwellirox.com/
- http://www.plomavi.com

These are some sites which I dislike:
1.) http://www.gallic-estatio.com/guides/france/rent/
2.) http://www.solohomvenu.co.za/property-rentals.htm

We don't need an HTML-coded design at this early project-stage. We only expect getting a simple bitmap or vector-graphic design. Maybe with the PSD-file (or wathever program you use) that we can pick-out some elements for building the prototype.

```html
<!DOCTYPE html>
<html lang="en">
<head>
<meta charset="utf-8">
<title>Lodgewell – Property Details</title>
<link href="https://fonts.googleapis.com/css2?family=Open+Sans:wght@400;600;700&family=PT+Sans+Narrow:wght@700&family=Lora:ital,wght@0,400;1,400&display=swap" rel="stylesheet">
<style>
:root{
  --teal:#16a9b0;
  --teal-dark:#0e8c93;
  --red:#d23c17;
  --sky:#85cae6;
  --ink:#333;
  --muted:#666;
  --line:#cfcfcf;
  --footer:#333333;
  --footer-line:#e0401c;
  --green:#3aa53a;
}
*{box-sizing:border-box;margin:0;padding:0}
html,body{width:1200px;height:2166px;overflow:hidden}
body{position:relative;background:#fff;font-family:"Open Sans",Arial,sans-serif;color:var(--ink);font-size:13px}
.abs{position:absolute}
.heading{font-family:"PT Sans Narrow","Arial Narrow",sans-serif;font-weight:700;color:var(--red);font-size:19px;text-transform:none}
/* top nav */
.topnav{left:0;top:0;width:1200px;height:80px;background:#fff}
.topnav ul{list-style:none;position:absolute;left:146px;top:28px;display:flex}
.topnav li{font-size:15px;color:#222;padding:0 20px;border-left:1px solid #bbb;line-height:20px}
.topnav li:first-child{border:none;padding-left:5px}
.topnav li.active{border-bottom:3px solid var(--teal);padding-bottom:8px}
.btn-dark{top:22px;height:34px;background:#2f2f2f;color:#fff;border-radius:4px;font-size:13px;display:flex;align-items:center;gap:8px;padding:0 14px}
/* hero */
.hero{left:0;top:80px;width:1200px;height:468px;background:linear-gradient(180deg,#4f6f8c 0%,#7a8fa2 30%,#c8a77a 62%,#5b6a3e 82%,#2f3a22 100%)}
.hero-arrow{top:293px;width:46px;height:46px;border-radius:50%;background:rgba(255,255,255,.85)}
.logo-box{left:130px;top:82px;width:196px;height:146px;background:#fff;border-radius:0 0 8px 8px;box-shadow:0 3px 8px rgba(0,0,0,.35);display:flex;flex-direction:column;align-items:center;justify-content:center;gap:12px}
.logo-mark{width:72px;height:52px;background:var(--teal);border-radius:6px}
.logo-name{font-family:"Lora",serif;font-size:28px;color:#444}
.tagline{right:130px;top:512px;font-family:"Lora",serif;font-style:italic;color:#fff;font-size:20px}
/* sidebar */
.side-card{left:130px;top:461px;width:264px;height:769px;background:#fff;border-radius:14px;box-shadow:-3px 4px 10px rgba(0,0,0,.25)}
.field{position:absolute;height:30px;border:1px solid #bdbdbd;background:#fff;font-size:13px;padding-left:10px;display:flex;align-items:center}
.btn-teal{position:absolute;background:linear-gradient(#28bcc2,var(--teal-dark));color:#fff;font-weight:700;font-size:14px;display:flex;align-items:center;justify-content:center;border-radius:3px}
.dotted{position:absolute;border-top:2px dotted #bbb}
/* main */
.infobar{left:470px;top:615px;width:598px;height:32px;border:1px solid var(--line);display:flex;font-size:13px}
.infobar div{flex:1;display:flex;align-items:center;justify-content:center;border-right:1px solid var(--line)}
.infobar div:last-child{border:none}
.infobar b{margin-right:6px}
.infobar span{color:#888}
.photo{background:linear-gradient(135deg,#c9ced3,#8d8f8c 55%,#5e5147)}
.thumbs{left:468px;top:918px;width:600px;height:111px;background:#d9d9d9;display:flex;gap:20px;padding:9px 12px}
.thumbs div{flex:1;border:3px solid #fff}
.desc{left:468px;top:1090px;width:602px;font-size:11.4px;line-height:17.5px;letter-spacing:-0.15px;color:#444}
.amen{left:472px;top:1215px;width:600px;display:grid;grid-template-columns:156px 160px 143px 140px;row-gap:5px;font-size:12.5px}
.amen div{display:flex;align-items:center;gap:10px;height:18px}
.tick{width:14px;height:14px}
.dot{width:8px;height:8px;border-radius:50%;background:#999;margin:0 3px}
.map{left:470px;top:1445px;width:598px;height:195px;background:linear-gradient(135deg,#e6e2d4,#d9d6c8 50%,#e9e4cf)}
.portrait{left:474px;top:1707px;width:132px;height:132px;border-radius:50%;border:4px solid #ddd;background:linear-gradient(#dfe5ea,#9aa6b1)}
.review{left:636px;top:1718px;width:432px;font-size:12.5px;line-height:21px;color:#444}
/* calendar */
.cal{left:132px;top:1629px;width:262px;height:219px;background:#f4f2e6;box-shadow:2px 3px 6px rgba(0,0,0,.3)}
.cal-head{height:44px;background:var(--sky);display:flex;align-items:center;justify-content:center;font-family:"PT Sans Narrow",sans-serif;font-weight:700;font-size:27px;color:#123}
.cal table{width:100%;border-collapse:collapse;font-size:13px;font-weight:700;text-align:center;margin-top:6px}
.cal td{height:28px}
.cal .sun{color:var(--red)}
/* footer */
.footer{left:0;top:1910px;width:1200px;height:224px;background:var(--footer);border-top:7px solid var(--footer-line);color:#ddd}
.footer h4{font-family:"PT Sans Narrow",sans-serif;font-size:20px;color:#6ec6e6;font-weight:700;text-transform:uppercase}
.fcol{position:absolute;top:40px}
.fcol ul{list-style:none;margin-top:12px;font-size:12px;line-height:21px}
.fcol li::before{content:"› ";color:#aaa}
.vsep{position:absolute;top:30px;width:1px;height:170px;background:#555}
.social{display:flex;align-items:center;gap:14px;font-size:13px;margin-top:12px}
.social i{width:26px;height:26px;border-radius:50%;background:#ddd;display:block}
.bottom{left:0;top:2134px;width:1200px;height:32px;background:var(--sky);font-size:12px;display:flex;align-items:center;justify-content:center;color:#234}
</style>
</head>
<body>

<nav class="abs topnav">
  <ul>
    <li class="active">Home</li><li>About Us</li><li>Features</li><li>Popular Properties</li><li>Contact Us</li>
  </ul>
  <div class="abs btn-dark" style="left:866px">
    <svg width="14" height="14" viewBox="0 0 14 14"><rect x="1" y="1" width="12" height="12" fill="none" stroke="#fff" stroke-width="1.5"/><path d="M3 7h6M7 4l3 3-3 3" stroke="#fff" stroke-width="1.5" fill="none"/></svg>Login</div>
  <div class="abs btn-dark" style="left:966px">
    <svg width="14" height="14" viewBox="0 0 14 14"><rect x="1" y="2" width="10" height="11" fill="none" stroke="#fff" stroke-width="1.5"/><path d="M6 9l7-7" stroke="#fff" stroke-width="1.8"/></svg>Register</div>
</nav>

<div class="abs hero" role="img" aria-label="Modern two-storey villa lit at dusk"></div>
<div class="abs hero-arrow" style="left:40px"><svg width="46" height="46"><path d="M27 14l-9 9 9 9" stroke="#333" stroke-width="4" fill="none"/></svg></div>
<div class="abs hero-arrow" style="left:1114px"><svg width="46" height="46"><path d="M19 14l9 9-9 9" stroke="#333" stroke-width="4" fill="none"/></svg></div>
<div class="abs logo-box"><div class="logo-mark"></div><div class="logo-name">Lodgewell</div></div>
<div class="abs tagline">for People who want to spend money to rent a good quality property.</div>

<!-- search sidebar -->
<aside class="abs side-card"></aside>
<div class="field" style="left:146px;top:490px;width:186px;font-size:11px;font-weight:700">SEARCH</div>
<div class="btn-teal" style="left:338px;top:490px;width:38px;height:30px;font-size:12px">GO</div>
<div class="abs heading" style="left:148px;top:551px">FIND YOUR PERFECT FIT.</div>
<div class="dotted" style="left:148px;top:584px;width:226px"></div>
<div class="field" style="left:148px;top:598px;width:224px">Location</div>
<div class="field" style="left:148px;top:645px;width:224px">Check in</div>
<div class="field" style="left:148px;top:693px;width:224px">Check out</div>
<div class="field" style="left:148px;top:742px;width:224px">4 Guest
  <svg class="abs" style="right:8px;top:10px" width="14" height="10"><path d="M0 0h14L7 10z" fill="#222"/></svg></div>
<svg class="abs" style="left:344px;top:652px" width="18" height="16"><rect x="1" y="2" width="16" height="13" fill="none" stroke="#777"/><path d="M1 6h16" stroke="#777"/></svg>
<svg class="abs" style="left:344px;top:700px" width="18" height="16"><rect x="1" y="2" width="16" height="13" fill="none" stroke="#777"/><path d="M1 6h16" stroke="#777"/></svg>
<div class="btn-teal" style="left:191px;top:799px;width:143px;height:30px">SEARCH</div>

<div class="abs heading" style="left:148px;top:872px">SPECIAL OFFERS</div>
<div class="dotted" style="left:148px;top:905px;width:226px"></div>
<div class="abs photo" style="left:147px;top:923px;width:230px;height:188px;background:linear-gradient(#1d3f6b,#4f6f90 50%,#2a8fb8 80%,#1b5670)" role="img" aria-label="Villa with lit pool at night"></div>
<div class="abs" style="left:147px;top:1083px;width:64px;height:28px;background:var(--teal);color:#fff;font-weight:700;display:flex;align-items:center;justify-content:center">$3650</div>
<div class="abs" style="left:147px;top:1124px;color:var(--red);font-size:15px">Lorem Ipsum dummy text</div>
<div class="abs" style="left:147px;top:1155px;width:220px;font-size:12px;line-height:18px">Lorem ipsum dummy text here lorem ipsum dummy data here.</div>
<div class="abs" style="left:326px;top:1197px;color:var(--red);font-size:12px;font-weight:700;text-decoration:underline">View All</div>

<!-- contact form -->
<div class="abs heading" style="left:134px;top:1255px">CONTACT FORM</div>
<div class="dotted" style="left:134px;top:1289px;width:244px"></div>
<div class="field" style="left:134px;top:1304px;width:244px;font-weight:600;font-size:12px">Name</div>
<div class="field" style="left:134px;top:1348px;width:244px;font-weight:600;font-size:12px">Email</div>
<div class="field" style="left:134px;top:1392px;width:244px;font-weight:600;font-size:12px">Phone</div>
<div class="field" style="left:134px;top:1438px;width:244px;height:96px;align-items:flex-start;padding-top:8px;font-weight:600;font-size:12px">Message</div>
<div class="btn-teal" style="left:134px;top:1557px;width:141px;height:31px">SUBMIT</div>

<!-- calendar -->
<div class="abs cal">
  <div class="cal-head">APRIL 2014</div>
  <table>
    <tr><td class="sun">Sun</td><td>Mon</td><td>Tue</td><td>Wed</td><td>Thu</td><td>Fri</td><td>Sat</td></tr>
    <tr><td></td><td></td><td>1</td><td>2</td><td>3</td><td>4</td><td>5</td></tr>
    <tr><td class="sun">6</td><td>7</td><td>8</td><td>9</td><td>10</td><td>11</td><td>12</td></tr>
    <tr><td class="sun">13</td><td>14</td><td>15</td><td>16</td><td>17</td><td>18</td><td>19</td></tr>
    <tr><td class="sun">20</td><td>21</td><td>22</td><td>23</td><td>24</td><td>25</td><td>26</td></tr>
    <tr><td class="sun">27</td><td>28</td><td>29</td><td>30</td><td></td><td></td><td></td></tr>
  </table>
</div>
<div class="abs" style="left:150px;top:1612px;width:30px;height:30px;border-radius:50%;background:#8a3fa8"></div>

<!-- main column -->
<div class="abs heading" style="left:468px;top:573px;font-size:19px">Home of your Dreams</div>
<div class="abs infobar">
  <div><b>Price:</b><span>$3650</span></div>
  <div><b>Beds:</b><span>6</span></div>
  <div><b>Baths:</b><span>3</span></div>
  <div><b>Area:</b><span>2,342</span></div>
  <div><b>Type:</b><span>Rent</span></div>
</div>
<div class="abs photo" style="left:468px;top:663px;width:600px;height:242px" role="img" aria-label="Bright living room with white sofa and city view"></div>
<svg class="abs" style="left:486px;top:765px" width="20" height="36"><path d="M16 2L4 18l12 16" stroke="#fff" stroke-width="4" fill="none"/></svg>
<svg class="abs" style="left:1030px;top:765px" width="20" height="36"><path d="M4 2l12 16L4 34" stroke="#fff" stroke-width="4" fill="none"/></svg>
<div class="abs thumbs">
  <div class="photo" role="img" aria-label="Living room thumbnail"></div>
  <div class="photo" role="img" aria-label="House exterior thumbnail" style="background:linear-gradient(#9fb8cf,#c9c1a8)"></div>
  <div class="photo" role="img" aria-label="Pool house thumbnail" style="background:linear-gradient(#a9c4dd,#7fa0a8)"></div>
  <div class="photo" role="img" aria-label="Suburban house thumbnail" style="background:linear-gradient(#b7cfe3,#b39c7e)"></div>
</div>

<div class="abs heading" style="left:468px;top:1054px;font-size:18px">Description</div>
<p class="abs desc">Vestibulum feugiat tempor mattis. Maecenas venenatis at erat sit amet viverra. Fusce sagittis pretium est vel iaculis. Proin vel tincidunt nisi. Sed non vehicula purus. In auctor sodales metus, ac fermentum odio sagittis quis. Curabitur volutpat, erat nec varius dapibus, felis libero malesuada mauris, at vestibulum enim erat non nibh. Donec ac nibh dapibus, sagittis libero a, sodales enim. Quisque a viverra mi.</p>

<div class="abs heading" style="left:468px;top:1173px;font-size:18px">Amenities</div>
<div class="abs amen">
  <div><svg class="tick"><path d="M2 7l4 4 7-9" stroke="#3aa53a" stroke-width="2.5" fill="none"/></svg>Air Conditioning</div>
  <div><i class="dot"></i>Balcony</div>
  <div><svg class="tick"><path d="M2 7l4 4 7-9" stroke="#3aa53a" stroke-width="2.5" fill="none"/></svg>Dishwasher</div>
  <div><i class="dot"></i>Use of pool</div>
  <div><svg class="tick"><path d="M2 7l4 4 7-9" stroke="#3aa53a" stroke-width="2.5" fill="none"/></svg>Cable TV</div>
  <div><i class="dot"></i>Cleaning after exit</div>
  <div><i class="dot"></i>Fridge</div>
  <div><svg class="tick"><path d="M2 7l4 4 7-9" stroke="#3aa53a" stroke-width="2.5" fill="none"/></svg>Parking</div>
  <div><i class="dot"></i>Computer</div>
  <div><svg class="tick"><path d="M2 7l4 4 7-9" stroke="#3aa53a" stroke-width="2.5" fill="none"/></svg>Cot</div>
  <div><svg class="tick"><path d="M2 7l4 4 7-9" stroke="#3aa53a" stroke-width="2.5" fill="none"/></svg>Heating</div>
  <div><svg class="tick"><path d="M2 7l4 4 7-9" stroke="#3aa53a" stroke-width="2.5" fill="none"/></svg>Toaster</div>
  <div><i class="dot"></i>DVD</div>
  <div><i class="dot"></i>Fan</div>
  <div><i class="dot"></i>Microwave</div>
  <div><svg class="tick"><path d="M2 7l4 4 7-9" stroke="#3aa53a" stroke-width="2.5" fill="none"/></svg>Terrace</div>
  <div><svg class="tick"><path d="M2 7l4 4 7-9" stroke="#3aa53a" stroke-width="2.5" fill="none"/></svg>Juicer</div>
  <div><svg class="tick"><path d="M2 7l4 4 7-9" stroke="#3aa53a" stroke-width="2.5" fill="none"/></svg>Hairdryer</div>
  <div><i class="dot"></i>Smoking allowed</div>
  <div><svg class="tick"><path d="M2 7l4 4 7-9" stroke="#3aa53a" stroke-width="2.5" fill="none"/></svg>Video</div>
  <div><i class="dot"></i>Oven</div>
  <div><i class="dot"></i>Internet</div>
  <div><i class="dot"></i>Towelwes</div>
  <div><svg class="tick"><path d="M2 7l4 4 7-9" stroke="#3aa53a" stroke-width="2.5" fill="none"/></svg>Roof terrace</div>
  <div><svg class="tick"><path d="M2 7l4 4 7-9" stroke="#3aa53a" stroke-width="2.5" fill="none"/></svg>Radio</div>
  <div><svg class="tick"><path d="M2 7l4 4 7-9" stroke="#3aa53a" stroke-width="2.5" fill="none"/></svg>Lift</div>
  <div><svg class="tick"><path d="M2 7l4 4 7-9" stroke="#3aa53a" stroke-width="2.5" fill="none"/></svg>Iron</div>
  <div><svg class="tick"><path d="M2 7l4 4 7-9" stroke="#3aa53a" stroke-width="2.5" fill="none"/></svg>Parquet</div>
</div>

<div class="abs heading" style="left:468px;top:1408px;font-size:18px">Location Map</div>
<div class="abs map" role="img" aria-label="Street map showing the property location"></div>
<svg class="abs" style="left:802px;top:1520px" width="22" height="30"><path d="M11 29C4 18 1 14 1 10a10 10 0 0 1 20 0c0 4-3 8-10 19z" fill="#e2231a"/><circle cx="11" cy="10" r="4" fill="#fff"/></svg>

<div class="abs heading" style="left:468px;top:1667px;font-size:18px">Customer Reviews</div>
<div class="dotted" style="left:468px;top:1697px;width:600px"></div>
<div class="abs" style="left:1012px;top:1672px;width:20px;height:20px;background:#555"><svg width="20" height="20"><path d="M12 5l-5 5 5 5" stroke="#fff" stroke-width="2" fill="none"/></svg></div>
<div class="abs" style="left:1038px;top:1672px;width:20px;height:20px;background:#555"><svg width="20" height="20"><path d="M8 5l5 5-5 5" stroke="#fff" stroke-width="2" fill="none"/></svg></div>
<div class="abs portrait" role="img" aria-label="Reviewer portrait"></div>
<p class="abs review"><span style="font-family:Lora,serif;font-size:28px;color:#888;vertical-align:-8px">“</span> Stibulum feugiat tempor mattis. Maecenas venenatis at erat sit amet viverra. Fusce sagittis pretium est vel iaculis. Proin vel tincidunt nisi. Sed non vehicula purus. In auctor sodales metus, ac fermentum odio sagittis quis. Curabitur volutpat, erat nec varius dapibus, felis libero malesuada mauris, at vestibulum enim erat non nibh. Donec ac nibh dapibus, sagittis libero a, sodales enim Quisque viverra... <span style="font-family:Lora,serif;font-size:28px;color:#888;vertical-align:-12px">”</span></p>
<div class="abs" style="left:968px;top:1842px;width:100px;text-align:right;color:var(--red);font-size:12px;font-weight:700">Customer Name</div>

<!-- footer -->
<footer class="abs footer">
  <div class="fcol" style="left:139px">
    <h4>Site Links</h4>
    <ul><li>Support</li><li>Get in touch</li><li>About us</li><li>Terms of use</li><li>Copyrights</li><li>Join us</li></ul>
  </div>
  <div class="vsep" style="left:283px"></div>
  <div class="fcol" style="left:338px;width:240px">
    <h4>Newsletter Form</h4>
    <p style="font-size:12px;line-height:18px;margin-top:10px">Get the latest &nbsp;updates by entering your email address.</p>
    <div style="margin-top:10px;width:228px;height:28px;background:#fff;color:#333;font-style:italic;font-size:12px;padding:6px 8px">Email Address</div>
    <div style="margin-top:14px;width:114px;height:30px;background:var(--teal);color:#fff;font-weight:700;font-size:13px;display:flex;align-items:center;justify-content:center">SUBSCRIBE</div>
  </div>
  <div class="vsep" style="left:613px"></div>
  <div class="fcol" style="left:663px;width:200px">
    <h4>Get in touch</h4>
    <div style="display:flex;gap:12px;font-size:12px;line-height:18px;margin-top:10px"><svg width="12" height="16" style="flex:none"><path d="M6 15C2 9 1 7 1 5a5 5 0 0 1 10 0c0 2-1 4-5 10z" fill="#e0401c"/></svg>Lorem ipsum dummy text here lorem ipsum text.</div>
    <div style="display:flex;gap:12px;font-size:12px;margin-top:14px"><svg width="12" height="14"><path d="M2 1h3l1 4-2 1c1 2 2 4 4 5l1-2 4 1v3c-7 0-11-5-11-12z" fill="#e0401c"/></svg>123-456-7890</div>
    <div style="display:flex;gap:12px;font-size:12px;margin-top:16px"><svg width="14" height="12"><rect x="1" y="1" width="12" height="10" fill="#e0401c"/><path d="M1 1l6 5 6-5" stroke="#fff" fill="none"/></svg>info@sample.com</div>
  </div>
  <div class="vsep" style="left:888px"></div>
  <div class="fcol" style="left:938px">
    <h4>Follow us on</h4>
    <div class="social"><i></i>Friendwall</div>
    <div class="social"><i></i>Chirpline</div>
    <div class="social"><i></i>Linkwork</div>
  </div>
</footer>
<div class="abs bottom">Copyright 2014 &nbsp;lodgewell.com</div>

</body>
</html>
```